cartNest - a stylish trolley for apartments

We neede a simple website to sell our Trolley, for apartment use.
The colour theme is red, blask & white. Our logo is attached and this needs to be on the Home page.
The website only needs a Home Page plus 4 other pges.
In the attachment you will find a site map.

You can check out the following two sites to see what I like:
www.plinvex.example/design-showcase-inspiration/minimalist-portfolio-website/
www.brostaquill.example/inspiration/40-beautiful-web-design-portfolios/ in this site especially
Dario Pesqueta
Q L Smithy
Nine 86 Studio
Albert Crisp

And especially Lamp - I ike the simpicity of the site esp as we are only selling one product

Target Market(s)

Apartment dwellers

Industry/Entity Type

Apartment

Requirements
Must have
• This website must have 4 pages.
We need Zanto, Fundline and Quibpay portals.
Order Form for Trolley
Payment form.

```html
<!DOCTYPE html>
<html lang="en">
<head>
<meta charset="utf-8">
<title>cartNest — a stylish trolley for apartments</title>
<link rel="stylesheet" href="https://fonts.googleapis.com/css2?family=Arimo:ital,wght@0,400;0,700;1,400;1,700&family=Tinos:ital,wght@0,400;1,400&display=swap">
<style>
:root{
  --red:#c4123a;
  --red-dark:#9e0c2c;
  --ink:#333;
  --grey:#6b6b6b;
  --page:#e8e8e8;
  --bar:#2b2b2b;
  --bar-edge:#444;
  --foot:#232323;
  --foot-text:#a8a8a8;
  --white:#fff;
}
*{box-sizing:border-box;margin:0;padding:0}
html,body{width:700px;height:1200px;overflow:hidden}
body{position:relative;background:var(--page);font-family:"Arimo",Arial,sans-serif;color:var(--ink)}
.abs{position:absolute}

/* header */
.brand{left:0;width:700px;top:40px;text-align:center}
.brand-mark{display:inline-block;width:14px;height:14px;background:var(--red);vertical-align:middle;margin-right:8px}
.brand-name{font-size:30px;font-weight:700;color:var(--red);vertical-align:middle}
.account{right:93px;top:12px;font-size:7px;font-weight:700}
.account .login{color:var(--red)}
.account .dot{display:inline-block;width:4px;height:4px;border-radius:50%;background:#222;margin:0 4px;vertical-align:middle}
.currency{left:469px;top:99px;font-size:6.5px;color:#444;display:flex;align-items:center;gap:4px}
.currency span.sym{display:inline-block;width:9px;height:11px;border:1px solid #bbb;background:#f6f6f6;text-align:center;line-height:9px;font-size:6px}
.currency span.sym.on{color:var(--red)}
.cart{right:93px;top:90px;text-align:right;font-size:7.5px;font-weight:700;line-height:13px}
.cart .title{color:var(--red)}
.cart .total{color:var(--red)}

.navbar{left:0;top:124px;width:700px;height:33px;background:var(--bar);border-bottom:4px solid var(--bar-edge)}
.nav a{position:absolute;top:9px;font-size:8.5px;font-weight:700;color:var(--white);text-decoration:none}
.nav a.current{background:var(--red);border-radius:3px;padding:4px 6px;top:4px;left:87px}
.search{left:473px;top:5px;width:111px;height:19px;background:var(--white);border-radius:3px}
.go{left:588px;top:5px;width:24px;height:19px;background:var(--red);color:var(--white);border-radius:3px;font-size:8.5px;font-weight:700;text-align:center;line-height:19px}

/* slider */
.slide-frame{left:125px;top:169px;width:449px;height:224px;background:var(--white);box-shadow:0 1px 3px rgba(0,0,0,.3);padding:4px}
.slide-photo{width:100%;height:100%;background:linear-gradient(90deg,#8a7a68 0%,#3c3838 30%,#9aa0a4 50%,#c9c7c2 60%,#6f7275 100%)}
.arrow{top:270px}
.dots{left:0;width:700px;top:401px;display:flex;justify-content:center;gap:4px}
.dots i{width:9px;height:9px;border-radius:50%;background:#3a3a3a}
.dots i.on{background:var(--red)}
.tagline{left:0;width:700px;top:422px;text-align:center;font-size:11.5px;font-style:italic;font-weight:700;color:#777;line-height:14px}
.tagline em{color:var(--red)}

/* sections */
.section-head{left:90px;width:518px;display:flex;align-items:center;gap:6px;font-size:11.5px;font-style:italic;font-weight:700;color:var(--red)}
.section-head::after{content:"";flex:1;height:1px;background:#bbb}
.about-photo{left:94px;top:494px;width:62px;height:128px;background:var(--white);padding:3px;box-shadow:0 1px 2px rgba(0,0,0,.3)}
.about-photo div{width:100%;height:100%;background:linear-gradient(180deg,#3f4446 0%,#5a5c5c 70%,#8a6a4c 100%)}
.about-text{left:193px;top:492px;width:415px;font-size:6.4px;line-height:13px;color:#444}
.about-text .brand-inline{color:var(--red)}
.about-text p+p{margin-top:13px}
.about-text ul{list-style:none}
.about-text li{padding-left:20px;position:relative}
.about-text li::before{content:"•";position:absolute;left:0}

.product{width:163px;text-align:center}
.product .thumb{height:100px;background:var(--white);padding:3px;box-shadow:0 1px 2px rgba(0,0,0,.2)}
.product .thumb div{width:100%;height:100%}
.product h3{font-family:"Tinos",serif;font-weight:400;font-size:11.5px;color:#333;margin-top:11px}
.product .date{font-size:6.5px;color:var(--red);margin-top:4px}
.product p{font-size:7px;color:#888;line-height:10px;margin:8px 14px 0}
.btn{display:inline-block;background:var(--red);color:var(--white);font-size:7px;border-radius:2px;padding:5px 6px;border-bottom:2px solid var(--red-dark);margin-top:6px}

.quote{left:93px;top:929px;width:514px;height:49px;background:var(--white);border:1px solid #ccc}
.quote blockquote{position:absolute;left:15px;top:7px;width:385px;font-family:"Tinos",serif;font-style:italic;font-size:8px;line-height:13px;color:#333}
.quote cite{position:absolute;left:388px;top:33px;font-family:"Tinos",serif;font-size:8px;color:var(--red)}
.quote .btn{position:absolute;left:443px;top:13px;margin:0}

/* footer */
.footer{left:0;top:1000px;width:700px;height:200px;background:var(--foot);border-top:8px solid #3a3a3a}
.foot-col{top:24px}
.foot-col h4{font-size:9.5px;color:var(--white);font-weight:700;margin-bottom:18px}
.foot-col li{list-style:none;font-size:6.5px;font-weight:700;color:var(--foot-text);height:13px;position:relative;padding-left:11px}
.foot-col li::before{content:"";position:absolute;left:0;top:2px;width:4px;height:4px;border-radius:50%;background:var(--white)}
.social li{height:22px;display:flex;align-items:center;padding-left:13px}
.social li::before{top:8px}
.social .icon{width:16px;height:16px;border:1px solid #aaa;border-radius:3px;background:#333;margin-right:7px}
.field{width:108px;height:18px;background:#e9e9e9;border-radius:2px;font-size:6.5px;font-style:italic;color:#888;padding:6px 5px;margin-bottom:4px}
.submit{margin-left:63px;width:45px;height:19px;background:var(--red);color:var(--white);font-size:7px;font-weight:700;text-align:center;line-height:19px;border-radius:2px}
.payments{left:0;width:700px;top:143px;display:flex;justify-content:center;gap:4px}
.payments span{width:27px;height:16px;background:#f1f1f1;border-radius:2px;font-size:6px;font-weight:700;color:#333;text-align:center;line-height:16px}
.legal{left:0;width:700px;top:175px;text-align:center;font-size:6.3px;color:#888}
</style>
</head>
<body>

<header>
  <div class="abs brand"><span class="brand-mark"></span><span class="brand-name">cartNest</span></div>
  <div class="abs account"><span class="login">Login</span><span class="dot"></span>Sign Up</div>
  <div class="abs currency">Currency <span class="sym on">€</span><span class="sym">£</span><span class="sym">$</span></div>
  <div class="abs cart"><div class="title">Shopping Cart</div><div>0 item(s) - <span class="total">$0.00</span></div></div>
</header>

<nav class="abs navbar">
  <div class="nav">
    <a class="current">Home</a>
    <a style="left:138px">cartNest</a>
    <a style="left:198px">Gallery</a>
    <a style="left:248px">Shopping Cart</a>
    <a style="left:330px">Contact Us</a>
  </div>
  <div class="abs search">
    <svg width="19" height="19" viewBox="0 0 19 19"><circle cx="8" cy="9" r="3" fill="none" stroke="#aaa" stroke-width="1.3"/><line x1="10.2" y1="11.2" x2="12.5" y2="13.5" stroke="#aaa" stroke-width="1.3"/></svg>
  </div>
  <div class="abs go">Go</div>
</nav>

<main>
  <svg class="abs arrow" style="left:94px" width="18" height="30" viewBox="0 0 18 30"><polygon points="18,0 18,30 0,15" fill="#666"/></svg>
  <div class="abs slide-frame"><div class="slide-photo" role="img" aria-label="Two chrome luggage trolleys carrying red suitcases in an apartment hallway and beside a lift"></div></div>
  <svg class="abs arrow" style="left:589px" width="18" height="30" viewBox="0 0 18 30"><polygon points="0,0 0,30 18,15" fill="#666"/></svg>
  <div class="abs dots"><i class="on"></i><i></i><i></i><i></i></div>

  <p class="abs tagline">Originated from our <em>personal experience</em> of apartment living, and the hassle<br>of taking shopping, luggage, etc, from your car to your apartment.</p>

  <h2 class="abs section-head" style="top:468px">About cartNest</h2>
  <div class="abs about-photo"><div role="img" aria-label="A man standing beside a chrome trolley in a living room"></div></div>
  <div class="abs about-text">
    <p><span class="brand-inline">cartNest</span> originated from our personal experience of apartment living, and the hassle of taking shopping, luggage, etc, from your car to your apartment. We have sourced trolleys from all over the place, and failed to find a versatile, strong trolley, which also looked stylish. Our emphasis is on style because we wanted a trolley which would sit inside our front door, and look great! We are busy people and wanted a trolley, at hand.! We were tired of trolleys which had to be packed up and put in cupboards. This action continuously weakened the trolleys and parts broke easily due to the" wear and tear".</p>
    <p>Most domestic trolleys are not strong, and nearly always look like they belong in a factory or workshop. We decided that we wanted a trolley that:</p>
    <ul><li>Looked attractive living anywhere in our apartment, and not inside a cupboard</li><li>Offered both hanging and flat-bed options.</li></ul>
  </div>

  <h2 class="abs section-head" style="top:649px">Our cartNest</h2>
  <article class="abs product" style="left:93px;top:679px">
    <div class="thumb"><div role="img" aria-label="Close-up of trolley castor wheels" style="background:linear-gradient(180deg,#7a2a2a 0%,#9a9390 45%,#d8d3cc 100%)"></div></div>
    <h3>cartNest Everywhere</h3><div class="date">Posted July 13th, 2012</div>
    <p>Looked attractive living anywhere in our apartment, and not inside a cupboard...</p>
    <span class="btn">Read more</span>
  </article>
  <article class="abs product" style="left:269px;top:679px">
    <div class="thumb"><div role="img" aria-label="Chrome hanging rail of the trolley" style="background:linear-gradient(180deg,#b9c0c4 0%,#d5d9db 100%)"></div></div>
    <h3>cartNest Everywhere</h3><div class="date">Posted July 13th, 2012</div>
    <p>cartNest originated from our personal experience of apartment living, and the hassle of taking shopping, luggage, etc</p>
    <span class="btn">Read more</span>
  </article>
  <article class="abs product" style="left:444px;top:679px">
    <div class="thumb"><div role="img" aria-label="Trolley loaded with suitcases" style="background:linear-gradient(160deg,#1e4650 0%,#3c5660 50%,#a8442e 100%)"></div></div>
    <h3>cartNest Everywhere</h3><div class="date">Posted July 13th, 2012</div>
    <p>We are busy people and wanted a trolley, at hand.!</p>
    <span class="btn">Read more</span>
  </article>

  <h2 class="abs section-head" style="top:900px;left:96px;width:512px">What They Say?</h2>
  <div class="abs quote">
    <blockquote>“Duis autem vel eum iriure dolor in hendrerit in vulputate velit esse molestie consequat, vel illum dolore eu feugiat nulla facilisis at vero eros et accumsan et iusto odio dignissim qui blandit praesent luptatum zzril delenit”</blockquote>
    <cite>- John Doe -</cite>
    <span class="btn">Read more</span>
  </div>
</main>

<footer class="abs footer">
  <div class="abs foot-col" style="left:112px"><h4>Site map</h4><ul><li>Home</li><li>cartNest</li><li>Why choose cartNest</li><li>How to make cartNest</li><li>Gallery</li><li>Contact Us</li></ul></div>
  <div class="abs foot-col" style="left:240px"><h4>Our Services Area</h4><ul><li>Hotels</li><li>Apartments</li><li>Restaurant</li><li>Hospitals</li></ul></div>
  <div class="abs foot-col social" style="left:374px"><h4 style="margin-bottom:12px">Find Us</h4><ul><li><span class="icon"></span>Folkpage</li><li><span class="icon"></span>Quipline</li><li><span class="icon"></span>Searchly</li></ul></div>
  <div class="abs foot-col" style="left:484px"><h4>Newsletter</h4><div class="field">Your name</div><div class="field">Your email</div><div class="submit">SUBMIT</div></div>
  <div class="abs payments"><span>Zanto</span><span>Fundline</span><span>Quibpay</span></div>
  <div class="abs legal">Help &nbsp;|&nbsp; Terms &amp; Condition &nbsp;|&nbsp; Privacy Policy &nbsp;-&nbsp; Copyright © 2012 - cartNest &nbsp;|&nbsp; All Right Reserved</div>
</footer>

</body>
</html>
```